Business card for a plastic surgeon

i need a business card for a plastic surgeon. I have two adresses. The card should communicate safety, simmetry, beauty and with soft colors.
What i want in the card:
- my logo: Letters "R"and "B" (picture uploaded)
- my name: Renato Bastiani
- my registration: CRM 507 219
- my adresses and phone numbers (2):
- Av Dr Teixeira Lopes, 2710, sala 305 - Vila Olímpia | São Paulo/ SP - Phone: 11 4172-5036
- Al. Itapeva, 47, 3 andar - Alphaville | Barueri/ SP - Phone: 11 6350-2481

- my social network: site, facebook and instagram

Target Market(s)

people (95% girls and women) that want cosmetic procedures and plastic surgery

Industry/Entity Type

Business

Contact Information for Business Card

The card should communicate safety, simmetry, beauty and with soft colors.
Beige, brown, gray, rosy are some options. Color is free

Font styles to use
Serif

Requirements
Must have
• - my logo: Letters "R"and "B" (picture uploaded)
• - my name: Renato Bastiani
• - my registration: CRM 507 219
• - my adresses and phone numbers (2):
• - Av Dr Teixeira Lopes, 2710, sala 305 - Vila Olímpia | São Paulo/ SP - Phone: 11 4172-5036
• - Al. Itapeva, 47, 3 andar - Alphaville | Barueri/ SP - Phone: 11 6350-2481
• - my social network: site, facebook and instagram
Should not have
• other images (only my logo)

```html
<!DOCTYPE html>
<html lang="pt-BR">
<head>
<meta charset="utf-8">
<title>Renato Bastiani – Business Card</title>
<link rel="stylesheet" href="https://fonts.googleapis.com/css2?family=Cinzel:wght@400;500&family=Marcellus&display=swap">
<style>
  :root {
    --backdrop: #e6e6e8;
    --card-dark: #3a3d45;
    --card-light: #ffffff;
    --ink-dark: #1c1d21;
    --gold: #c9a35c;
    --gold-deep: #8a6128;
    --gold-light: #f3d98e;
  }
  * { margin: 0; padding: 0; box-sizing: border-box; }
  html, body { width: 1200px; height: 800px; overflow: hidden; }
  body {
    background: var(--backdrop);
    position: relative;
    font-family: "Marcellus", serif;
  }
  .card {
    position: absolute;
    left: 344px;
    width: 512px;
    height: 286px;
    border-radius: 14px;
    overflow: hidden;
  }
  /* Front side */
  .card--front { top: 60px; display: flex; }
  .front__brand {
    width: 256px;
    background: var(--card-light);
    display: flex;
    flex-direction: column;
    align-items: center;
    justify-content: center;
    padding-top: 10px;
  }
  .front__info {
    flex: 1;
    background: var(--card-dark);
    padding: 22px 16px 0 12px;
    color: var(--gold);
  }
  .front__name {
    font-family: "Marcellus", serif;
    font-size: 27px;
    font-weight: 400;
    color: var(--gold-light);
    white-space: nowrap;
    margin-bottom: 12px;
  }
  .front__details {
    list-style: none;
    text-align: right;
    font-size: 11px;
    line-height: 14px;
  }
  .front__details .gap { margin-top: 1px; }
  .front__details .web { font-size: 12.5px; margin-top: 2px; }
  .front__details .crm { margin-top: 6px; }

  /* Logo lockup (text only) */
  .brand-mark {
    display: flex;
    flex-direction: column;
    align-items: center;
  }
  .brand-mark__dot {
    width: 14px;
    height: 14px;
    border-radius: 50%;
    background: var(--ink-dark);
    margin-bottom: 16px;
  }
  .brand-mark__name {
    font-family: "Cinzel", serif;
    font-weight: 400;
    color: var(--ink-dark);
    letter-spacing: 0.5px;
    white-space: nowrap;
  }
  .brand-mark__role {
    font-family: "Cinzel", serif;
    color: var(--ink-dark);
    text-transform: uppercase;
    white-space: nowrap;
  }
  .front__brand .brand-mark__name { font-size: 15px; }
  .front__brand .brand-mark__role { font-size: 8px; letter-spacing: 1.6px; margin-top: 3px; }

  /* Back side */
  .card--back { top: 420px; background: var(--card-dark); }
  .back__stripe {
    position: absolute;
    top: 0;
    left: 448px;
    width: 20px;
    height: 100%;
    background: linear-gradient(180deg, var(--gold-deep) 0%, var(--gold) 45%, var(--gold-light) 75%, var(--gold) 100%);
  }
  .back__brand {
    position: absolute;
    left: 0;
    top: 0;
    width: 448px;
    height: 100%;
    display: flex;
    align-items: center;
    justify-content: center;
    padding-top: 12px;
  }
  .back__brand .brand-mark__name { font-size: 22px; }
  .back__brand .brand-mark__role { font-size: 11px; letter-spacing: 2.4px; margin-top: 4px; }
  .back__brand .brand-mark__dot { width: 18px; height: 18px; margin-bottom: 22px; }
</style>
</head>
<body>
  <section class="card card--front" aria-label="Card front">
    <div class="front__brand">
      <div class="brand-mark">
        <span class="brand-mark__dot"></span>
        <span class="brand-mark__name">DR. RENATO BASTIANI</span>
        <span class="brand-mark__role">Cirurgião Plástico</span>
      </div>
    </div>
    <div class="front__info">
      <h1 class="front__name">Renato Bastiani</h1>
      <ul class="front__details">
        <li>Av Dr Teixeira Lopes, 2710,</li>
        <li>sala 305 Vila Olímpia | São Paulo/ SP</li>
        <li>Phone: 11 4172-5036</li>
        <li class="gap">Al. Itapeva, 47, 3 andar</li>
        <li>Alphaville | Barueri/ SP</li>
        <li>Phone: 11 6350-2481</li>
        <li class="web">www.renatobastiani.com</li>
        <li class="crm">Registration: CRM 507 219</li>
      </ul>
    </div>
  </section>

  <section class="card card--back" aria-label="Card back">
    <div class="back__brand">
      <div class="brand-mark">
        <span class="brand-mark__dot"></span>
        <span class="brand-mark__name">DR. RENATO BASTIANI</span>
        <span class="brand-mark__role">Cirurgião Plástico</span>
      </div>
    </div>
    <div class="back__stripe"></div>
  </section>
</body>
</html>
```